Quillbrooks Menu Re-Design

Looking to update this menu.

Word doc of menu instructions is uploaded along with photos.

Please estimate cost for completion and expect at least 2-3 rounds of changes.

Thanks!

```html
<!DOCTYPE html>
<html lang="en">
<head>
<meta charset="utf-8">
<title>Quillbrooks Menu</title>
<link rel="stylesheet" href="https://fonts.googleapis.com/css2?family=Ubuntu:wght@300;400&family=Quicksand:wght@400;500&display=swap">
<style>
  :root {
    --paper: #ede4d0;
    --paper-light: #f3ead3;
    --wood-dark: #4e4740;
    --wood-light: #8a8279;
    --brand-red: #a8261d;
    --ink: #2a2522;
    --body-ink: #3b3431;
  }
  * { margin: 0; padding: 0; box-sizing: border-box; }
  html, body { width: 731px; height: 1200px; overflow: hidden; }
  body {
    position: relative;
    background: linear-gradient(160deg, var(--paper) 0%, var(--paper) 55%, var(--paper-light) 100%);
    font-family: "Quicksand", sans-serif;
    color: var(--body-ink);
  }
  .wood-strip {
    position: absolute; left: 0; top: 0; width: 78px; height: 1200px;
    background: linear-gradient(90deg, var(--wood-dark) 0%, var(--wood-light) 45%, #6d665e 70%, var(--wood-dark) 100%);
  }
  .section-badge {
    position: absolute; left: 19px; width: 66px; height: 66px;
    border-radius: 50%; background: var(--brand-red);
  }
  .section-title {
    position: absolute; left: 90px;
    font-family: "Ubuntu", sans-serif; font-weight: 400; font-size: 37px;
    color: var(--ink); white-space: nowrap; letter-spacing: 0.2px;
  }
  .section-note {
    font-family: "Quicksand", sans-serif; font-size: 11px; letter-spacing: 0;
    color: var(--body-ink); margin-left: 2px;
  }
  .item { position: absolute; width: 282px; }
  .item-name {
    font-family: "Ubuntu", sans-serif; font-weight: 400; font-size: 19px;
    color: var(--brand-red); line-height: 22px; white-space: nowrap;
  }
  .item-desc { font-size: 11.2px; line-height: 14px; margin-top: 0; }
  .price { float: right; }
  .options { margin-top: 3px; font-size: 11.2px; line-height: 14px; }
  .options div { display: flex; padding-left: 170px; }
  .options span:first-child { width: 60px; }
  .left { left: 90px; }
  .right { left: 395px; }
</style>
</head>
<body>
  <div class="wood-strip" role="img" aria-label="Weathered wood plank border"></div>

  <!-- Starters -->
  <div class="section-badge" style="top:80px" role="img" aria-label="Starters icon"></div>
  <h1 class="section-title" style="top:88px">Starters and Sharables</h1>

  <div class="item left" style="top:136px">
    <h2 class="item-name">Artichoke and Spinich Dip</h2>
    <p class="item-desc">A blend of marinated artichoke hearts, cream cheese, leaf spinach, and sharp parmesan. Accompanied with Quillbrooks bread and dipping veggies. <span class="price">8.99</span></p>
  </div>
  <div class="item left" style="top:207px">
    <h2 class="item-name">Bloomin’ Cactus</h2>
    <p class="item-desc">A sweet, colossal onion sliced to bloom, battered and fried to a golden brown. Served with Cactus Sauce. <span class="price">6.99</span></p>
  </div>
  <div class="item left" style="top:277px">
    <h2 class="item-name">Italian Nachos</h2>
    <p class="item-desc">Crispy wonton chips, Italian sausage, black olives, jalapenos, sliced peperoncinis, diced tomatoes, drizzled with rich Alfredo sauce and topped with melted mozzarella. <span class="price">9.99</span></p>
  </div>
  <div class="item right" style="top:135px">
    <h2 class="item-name">Fried Pickles</h2>
    <p class="item-desc">Our version of a Southern specialty. Dill pickle slices lightly hand breaded and golden fried. Served with homemade ranch dressing. <span class="price">4.99</span></p>
  </div>
  <div class="item right" style="top:207px">
    <h2 class="item-name">Buffalo Wings</h2>
    <p class="item-desc">Cool ’em down with our homemade bleu cheese dressing. <span class="price">6.99</span></p>
  </div>
  <div class="item right" style="top:278px">
    <h2 class="item-name">Loaded Cheese Fries</h2>
    <p class="item-desc">We mix in some bacon and sautéed onion, then melted cheddar cheese over the top. <span class="price">7.99</span></p>
  </div>

  <!-- Salads -->
  <div class="section-badge" style="top:433px" role="img" aria-label="Salads leaf icon"></div>
  <h1 class="section-title" style="top:445px">Salads<span class="section-note">These garden fresh salads are served with our freshly baked Quillbrooks’ bread or an apple.</span></h1>

  <div class="item left" style="top:489px">
    <h2 class="item-name">Caesar Salad</h2>
    <p class="item-desc">Tender, charbroiled chicken breast served on a bed of fresh Romaine lettuce, tossed with Caesar dressing, parmesan cheese, and croutons.</p>
    <div class="options"><div><span>Chicken</span><span>9.49</span></div><div><span>Salmon</span><span>12.49</span></div></div>
  </div>
  <div class="item left" style="top:581px">
    <h2 class="item-name">Fiesta Salad</h2>
    <p class="item-desc">Your choice of fajita beef or chicken with lettuce, shredded cheddar cheese, tomatoes, onions and croutons. Served with a side of pico de gallo.</p>
    <div class="options"><div><span>Beef</span><span>9.99</span></div><div><span>Chicken</span><span>9.49</span></div></div>
  </div>
  <div class="item left" style="top:673px">
    <h2 class="item-name">Rancher’s Salad</h2>
    <p class="item-desc">Seasoned strips of sautéed beef with grilled onions and mushrooms on a cool bed of greens. Sprinkled with diced tomatoes and bleu cheese crumbles. <span class="price">10.99</span></p>
  </div>
  <div class="item left" style="top:749px">
    <h2 class="item-name">Cobb Salad</h2>
    <p class="item-desc">Tender strips of chicken breast on a bed of fresh greens, tomato, onion, cheese, slices of hard-boiled boiled egg, diced bacon, crumbled bleu cheese, croutons and your choice of dressing. <span class="price">10.49</span></p>
  </div>
  <div class="item right" style="top:489px">
    <h2 class="item-name">Chicken Tender Salad</h2>
    <p class="item-desc">Crispy chicken tenders served hot over a bed of fresh lettuce, cheddar cheese, tomatoes, onions, and your choice of dressing. <span class="price">9.49</span></p>
  </div>
  <div class="item right" style="top:562px">
    <h2 class="item-name">Apple Orchard Salad</h2>
    <p class="item-desc">Sliced grilled chicken breast, fresh mixed greens, with cranberries, chopped walnuts, red onions and bleu cheese crumbles. Garnished with dried apple chips. <span class="price">11.49</span></p>
  </div>
  <div class="item right" style="top:640px; left:392px; width:285px">
    <h2 class="item-name">Chef Salad</h2>
    <p class="item-desc">Classic combination of sliced turkey, ham, Swiss cheese, and cheddar cheese mixed with salad greens, onions, tomatoes, topped with a sliced hard-boiled egg. <span class="price">10.49</span></p>
  </div>
  <div class="item right" style="top:717px; left:392px">
    <h2 class="item-name">Greek Salad</h2>
    <p class="item-desc">An authentic Mediterranean salad of tender chicken, juicy tomatoes, sliced red onion, crumbled feta cheese, and black olives. Served with Greek dressing. <span class="price">10.49</span></p>
  </div>

  <!-- Soups -->
  <div class="section-badge" style="top:917px" role="img" aria-label="Soup bowl icon"></div>
  <h1 class="section-title" style="top:929px">Soups<span class="section-note">All selections homemade in our kitchen and available every day.</span></h1>

  <div class="item left" style="top:977px">
    <h2 class="item-name">Chicken Enchilada Soup</h2>
    <p class="item-desc">Topped with pico de gallo and tortilla strips.</p>
  </div>
  <div class="item left" style="top:1020px">
    <h2 class="item-name">French Onion</h2>
    <p class="item-desc">Sweet caramelized onions in a savory broth. Crowned with baked mozzarella.</p>
    <div class="options" style="margin-top:19px"><div><span>Cup</span><span>2.99</span></div><div><span>Bowl</span><span>5.49</span></div></div>
  </div>
</body>
</html>
```